Glow Ridge inc New website
tanning salon
Thanks so much! We really like #18 and 19.
We like the colors on #15 and #13 too.
Like #12 and #14 - can the beds at the bottom be a scroll bar with lots of different bed pictures?
The images so far are not really our image. We have more hip yet conservative customer base. Any pics with men & women? Does not have to be on beach. Not using our old saying "we didn't invent tanning.... Please keep submitting!!
Like #2 better but not sure about the yellow up in the header by our logo.
Thanks.
Can you change the background to more of a yellow instead of brownish yellow?
Thanks!
I uploaded our logo.

```html
<!DOCTYPE html>
<html lang="en">
<head>
<meta charset="utf-8">
<title>Glow Ridge inc</title>
<link href="https://fonts.googleapis.com/css2?family=Open+Sans:wght@400;600;700&family=Roboto+Condensed:wght@700&display=swap" rel="stylesheet">
<style>
  :root {
    --page-top: #f4f4f4;
    --page-bottom: #e6e6e6;
    --top-band: #c9c9c9;
    --nav-bg: #d6d6d6;
    --nav-active: #1f7fd0;
    --ink: #222222;
    --muted: #555555;
    --soft: #777777;
    --sun: #f5a20a;
    --hero-light: #ffd23a;
    --hero-deep: #f59a00;
    --footer-bg: #d9d9d9;
    --icon-dark: #333333;
  }
  * { box-sizing: border-box; margin: 0; padding: 0; }
  html, body { width: 1200px; height: 706px; overflow: hidden; }
  body {
    font-family: "Open Sans", Arial, sans-serif;
    color: var(--ink);
    background: linear-gradient(var(--page-top), var(--page-bottom));
    position: relative;
  }
  .top-band { position: absolute; left: 0; top: 0; width: 1200px; height: 12px; background: var(--top-band); }
  .wrap { position: absolute; left: 240px; width: 720px; }
  .header { top: 36px; height: 80px; }
  .brand { position: absolute; left: 6px; top: 8px; display: flex; align-items: center; gap: 10px; }
  .brand-dot { width: 28px; height: 28px; border-radius: 50%; background: var(--sun); }
  .brand-name { font-weight: 700; font-size: 30px; color: var(--ink); letter-spacing: -0.5px; }
  .contact { position: absolute; right: 4px; top: 0; display: flex; gap: 26px; font-size: 11px; color: var(--muted); align-items: center; }
  .contact span { display: flex; align-items: center; gap: 8px; }
  .nav { top: 120px; height: 30px; background: var(--nav-bg); display: flex; align-items: center; }
  .nav a { font-size: 10.5px; font-weight: 600; color: var(--ink); text-decoration: none; padding: 0 22px; height: 30px; line-height: 30px; }
  .nav a.active { background: var(--nav-active); color: #fff; padding: 0 20px; }
  .social { margin-left: auto; display: flex; gap: 6px; padding-right: 8px; }
  .social i { width: 18px; height: 18px; background: #444; border-radius: 3px; display: block; }
  .hero { top: 168px; height: 288px; background: linear-gradient(100deg, var(--hero-light), var(--hero-deep)); overflow: hidden; }
  .hero h1 { position: absolute; left: 24px; top: 80px; font-family: "Roboto Condensed", Arial, sans-serif; font-weight: 700; font-size: 50px; line-height: 56px; color: #fff; text-transform: uppercase; }
  .hero h1 .line2 { display: block; padding-left: 96px; }
  .hero-photo { position: absolute; right: 0; top: 0; width: 330px; height: 288px; background: radial-gradient(ellipse at 55% 55%, #d8a486 0%, #e7b48a 35%, rgba(245,160,20,0) 70%); }
  .features { top: 490px; display: flex; }
  .feature { width: 240px; padding-left: 14px; display: grid; grid-template-columns: 48px 1fr; column-gap: 6px; }
  .feature h2 { font-size: 13px; font-weight: 700; align-self: center; }
  .feature p { grid-column: 2; font-size: 9px; line-height: 14px; color: var(--muted); margin-top: 6px; }
  .footer { position: absolute; left: 0; top: 614px; width: 1200px; height: 92px; background: var(--footer-bg); }
  .footer-inner { position: absolute; left: 240px; top: 24px; width: 720px; height: 50px; }
  .footer-links { font-size: 10px; color: var(--muted); }
  .footer-links a { color: var(--muted); text-decoration: none; }
  .footer-links .sep { margin: 0 6px; color: var(--soft); }
  .copyright { font-size: 10px; color: var(--soft); margin-top: 6px; }
  .to-top { position: absolute; left: 676px; top: 0; }
</style>
</head>
<body>
  <div class="top-band"></div>

  <header class="wrap header">
    <div class="brand"><span class="brand-dot"></span><span class="brand-name">Glow Ridge inc</span></div>
    <div class="contact">
      <span>
        <svg width="14" height="14" viewBox="0 0 14 14"><path d="M3 1l2.5 3-1.5 1.5c1 2 2.5 3.5 4.5 4.5L10 8.5l3 2.5-1.5 2C6 13 1 8 1 2.5z" fill="#333"/></svg>
        555-014-2290
      </span>
      <span>
        <svg width="16" height="12" viewBox="0 0 16 12"><rect x="0.5" y="0.5" width="15" height="11" fill="none" stroke="#333"/><path d="M0.5 0.5l7.5 6 7.5-6" fill="none" stroke="#333"/></svg>
        contact@glowridgeinc.com
      </span>
    </div>
  </header>

  <nav class="wrap nav">
    <a class="active" href="#">Home</a>
    <a href="#">Tanning Equipment</a>
    <a href="#">Tanning Options</a>
    <a href="#">Skin Care</a>
    <a href="#">Specials</a>
    <a href="#">Locations</a>
    <div class="social"><i></i><i></i><i></i></div>
  </nav>

  <section class="wrap hero">
    <h1>Look good ...<span class="line2">Feel great</span></h1>
    <div class="hero-photo" role="img" aria-label="Photo of a tanned model seated against the yellow backdrop"></div>
  </section>

  <section class="wrap features">
    <div class="feature">
      <svg width="44" height="28" viewBox="0 0 44 28"><path d="M8 24a14 14 0 0 1 28 0z" fill="var(--icon-dark)"/><g stroke="var(--icon-dark)" stroke-width="2"><line x1="22" y1="2" x2="22" y2="7"/><line x1="8" y1="8" x2="11" y2="11"/><line x1="36" y1="8" x2="33" y2="11"/><line x1="1" y1="24" x2="5" y2="24"/><line x1="39" y1="24" x2="43" y2="24"/></g></svg>
      <h2>SUNMIST TAN</h2>
      <p>Get your tan delivered by local spa experts.</p>
    </div>
    <div class="feature">
      <svg width="44" height="28" viewBox="0 0 44 28"><circle cx="16" cy="8" r="6" fill="var(--icon-dark)"/><path d="M4 28a12 12 0 0 1 24 0z" fill="var(--icon-dark)"/><circle cx="30" cy="10" r="5" fill="#666"/><path d="M22 28a10 10 0 0 1 18 0z" fill="#666"/></svg>
      <h2>CLUB</h2>
      <p>Drive visits and revenue and track loyalty.</p>
    </div>
    <div class="feature">
      <svg width="44" height="28" viewBox="0 0 44 28"><g stroke="var(--icon-dark)" stroke-width="2.5" stroke-linecap="round"><line x1="22" y1="2" x2="22" y2="7"/><line x1="22" y1="21" x2="22" y2="26"/><line x1="10" y1="14" x2="15" y2="14"/><line x1="29" y1="14" x2="34" y2="14"/><line x1="13.5" y1="5.5" x2="17" y2="9"/><line x1="27" y1="19" x2="30.5" y2="22.5"/><line x1="30.5" y1="5.5" x2="27" y2="9"/><line x1="17" y1="19" x2="13.5" y2="22.5"/></g></svg>
      <h2>SPECIALS</h2>
      <p>Scale your clients' results. We'll help make your look glow.</p>
    </div>
  </section>

  <footer class="footer">
    <div class="footer-inner">
      <div class="footer-links">
        <a href="#">Home</a><span class="sep">|</span><a href="#">Tanning Equipment</a><span class="sep">|</span><a href="#">Tanning Options</a><span class="sep">|</span><a href="#">Skin Care</a><span class="sep">|</span><a href="#">Specials</a><span class="sep">|</span><a href="#">Locations</a>
      </div>
      <div class="copyright">© 2012 Glow Ridge inc. All Rights Reserved</div>
      <svg class="to-top" width="30" height="30" viewBox="0 0 30 30" aria-label="Back to top"><circle cx="15" cy="15" r="14" fill="#222"/><path d="M15 7l7 8h-4.5v8h-5v-8H8z" fill="#fff"/></svg>
    </div>
  </footer>
</body>
</html>
```